RK LAW
Stationary Envelopes and Cards
RK LAW - Law
Creative Brief
Professional
Howard P. Lindqvist
Attorney At Law
347 N. 4th Avenue Las Vegas NV 89104
nvrklaw@mailbrook.net
NVRKLAW.NET

```html
<!DOCTYPE html>
<html lang="en">
<head>
<meta charset="utf-8">
<title>RK LAW – Business Card Concepts</title>
<link href="https://fonts.googleapis.com/css2?family=Cinzel:wght@400;600;700&display=swap" rel="stylesheet">
<style>
  :root {
    --bg: #2a2a2c;
    --card-white: #ffffff;
    --card-grey: #e6e6e6;
    --blue-deep: #0b3a9e;
    --blue-mid: #1657d0;
    --blue-light: #3d82ee;
    --gold: #d9a21c;
    --ink: #1d1d1f;
    --ink-soft: #4a4a4e;
    --label: #f1f1f1;
  }
  * { box-sizing: border-box; margin: 0; padding: 0; }
  html, body { width: 1200px; height: 914px; overflow: hidden; }
  body {
    background: var(--bg);
    font-family: "Cinzel", serif;
    position: relative;
  }
  .option-number {
    position: absolute;
    color: var(--label);
    font-size: 22px;
    font-family: Arial, sans-serif;
  }
  .card {
    position: absolute;
    width: 531px;
    height: 296px;
    border-radius: 16px;
    overflow: hidden;
    box-shadow: 0 6px 18px rgba(0,0,0,.55);
  }
  .card--white { background: linear-gradient(180deg, var(--card-white) 55%, var(--card-grey)); }
  .card--blue { background: radial-gradient(ellipse at 50% 45%, var(--blue-light) 0%, var(--blue-mid) 45%, var(--blue-deep) 100%); }
  .card > * { position: absolute; }

  .brand-dot {
    width: 40px; height: 40px;
    border-radius: 50%;
    background: var(--gold);
  }
  .brand-name {
    color: var(--gold);
    font-weight: 700;
    line-height: 1;
    white-space: nowrap;
  }
  .tagline {
    color: var(--blue-mid);
    font-size: 13px;
    letter-spacing: .5px;
    white-space: nowrap;
  }
  .person-name { font-weight: 700; font-size: 15px; color: var(--ink); white-space: nowrap; }
  .person-title { font-size: 11px; color: var(--ink-soft); }
  .address { font-size: 12px; color: var(--ink); line-height: 1.5; }
  .divider { width: 1px; background: #bdbdbd; }
  .contact-list { list-style: none; font-size: 12.5px; color: var(--ink); }
  .contact-list li { display: flex; align-items: center; gap: 10px; height: 19px; white-space: nowrap; }
  .contact-list svg { width: 12px; height: 12px; fill: var(--blue-mid); flex: none; }

  .footer-band {
    left: 0; right: 0; bottom: 0;
    height: 42px;
    background: linear-gradient(180deg, var(--blue-light), var(--blue-deep));
    border-top: 3px solid var(--gold);
    color: #fff;
    font-size: 12px;
    letter-spacing: 2px;
    display: flex; align-items: center; justify-content: center;
  }
  .centered { left: 0; right: 0; text-align: center; }
  .centered-dot { left: 245px; }
</style>
</head>
<body>

<svg width="0" height="0" style="position:absolute">
  <symbol id="icon-phone" viewBox="0 0 24 24"><path d="M6.6 10.8a15.1 15.1 0 0 0 6.6 6.6l2.2-2.2a1 1 0 0 1 1-.25 11.4 11.4 0 0 0 3.6.57 1 1 0 0 1 1 1V20a1 1 0 0 1-1 1A17 17 0 0 1 3 4a1 1 0 0 1 1-1h3.5a1 1 0 0 1 1 1c0 1.25.2 2.45.57 3.57a1 1 0 0 1-.25 1z"/></symbol>
  <symbol id="icon-fax" viewBox="0 0 24 24"><path d="M6 2h12v6H6zM3 9h18v9h-3v4H6v-4H3zm5 7v4h8v-4z"/></symbol>
  <symbol id="icon-mail" viewBox="0 0 24 24"><path d="M2 5h20v14H2zm2 2v.5l8 5 8-5V7zm0 3v7h16v-7l-8 5z"/></symbol>
</svg>

<span class="option-number" style="left:285px;top:28px">1</span>
<span class="option-number" style="left:880px;top:28px">2</span>
<span class="option-number" style="left:285px;top:445px">3</span>
<span class="option-number" style="left:880px;top:445px">4</span>

<!-- Option 1 -->
<section class="card card--white" style="left:44px;top:99px">
  <div class="brand-dot" style="left:106px;top:70px"></div>
  <div class="brand-name" style="left:37px;top:128px;font-size:36px">RK LAW</div>
  <div class="tagline" style="left:37px;top:168px">COUNSEL YOU CAN TRUST</div>
  <div class="divider" style="left:244px;top:56px;height:140px"></div>
  <div class="person-name" style="left:266px;top:58px">Howard P. Lindqvist</div>
  <div class="person-title" style="left:266px;top:80px">Attorney At Law</div>
  <div class="address" style="left:266px;top:108px">347 N. 4th Avenue<br>Las Vegas NV 89104</div>
  <ul class="contact-list" style="left:266px;top:156px">
    <li><svg><use href="#icon-phone"/></svg>(702) 555-0182</li>
    <li><svg><use href="#icon-fax"/></svg>(702) 555-0197</li>
    <li><svg><use href="#icon-mail"/></svg>NVRKLAW@MAILBROOK.NET</li>
  </ul>
  <div class="footer-band">WWW.NVRKLAW.NET</div>
</section>

<!-- Option 2 -->
<section class="card card--blue" style="left:622px;top:99px">
  <div class="brand-dot centered-dot" style="top:62px"></div>
  <div class="brand-name centered" style="top:126px;font-size:46px">RK LAW</div>
  <div class="tagline centered" style="top:178px;color:#e8eefc;font-size:15px">COUNSEL YOU CAN TRUST</div>
</section>

<!-- Option 3 -->
<section class="card card--white" style="left:44px;top:514px">
  <div class="brand-dot" style="left:124px;top:40px"></div>
  <div class="brand-name" style="left:186px;top:38px;font-size:36px">RK LAW</div>
  <div class="tagline" style="left:186px;top:76px">COUNSEL YOU CAN TRUST</div>
  <div class="person-name" style="left:34px;top:140px">Howard P. Lindqvist</div>
  <div class="person-title" style="left:34px;top:161px">Attorney At Law</div>
  <div class="address" style="left:34px;top:188px">347 N. 4th Avenue<br>Las Vegas NV 89104</div>
  <div class="divider" style="left:258px;top:138px;height:90px"></div>
  <ul class="contact-list" style="left:278px;top:150px">
    <li><svg><use href="#icon-phone"/></svg>(702) 555-0182</li>
    <li><svg><use href="#icon-fax"/></svg>(702) 555-0197</li>
    <li><svg><use href="#icon-mail"/></svg>NVRKLAW@MAILBROOK.NET</li>
  </ul>
  <div class="footer-band">WWW.NVRKLAW.NET</div>
</section>

<!-- Option 4 -->
<section class="card card--white" style="left:622px;top:514px">
  <div class="brand-dot centered-dot" style="top:62px"></div>
  <div class="brand-name centered" style="top:124px;font-size:46px">RK LAW</div>
  <div class="tagline centered" style="top:176px;font-size:15px">COUNSEL YOU CAN TRUST</div>
</section>

</body>
</html>
```